Modern Billboard Ad for Criminal Defense Firm

10.5 x 36 We're looking for something to set us apart from the local competition. Looking for sleek and modern. We're a mid-sized firm in a small market city. We want to give the artist room to be creative on this one.
Thanks

Target Market(s)

Adult clients who have been charged with a crime/DWI

Industry/Entity Type

legal

Font styles to use
Serif
Sans Serif

Requirements
Must have
• Needs to have the firm name in large lettering. Law Offices of Marcus T Whitfield. “PLLC” does not have to be included. Phone number of (555) 384-1927 should be included but not the main focus.
Nice to have
• A call to action or something similar. “Don’t go it alone, call today.”, “ Arrested?”

```html
<!DOCTYPE html>
<html lang="en">
<head>
<meta charset="utf-8">
<title>Law Offices of Marcus T Whitfield – Billboard</title>
<link href="https://fonts.googleapis.com/css2?family=Alfa+Slab+One&family=Fira+Sans+Condensed:wght@500&display=swap" rel="stylesheet">
<style>
  :root {
    --sky: #29a9e1;
    --sky-star: #7cc3ec;
    --ink: #050607;
    --white: #ffffff;
    --suit-light: #b4b6b9;
    --suit-dark: #6f7276;
  }
  html, body {
    margin: 0;
    padding: 0;
    overflow: hidden;
    background: var(--white);
  }
  .billboard {
    position: relative;
    width: 1200px;
    height: 350px;
    overflow: hidden;
    background: var(--ink);
  }
  .star-band {
    position: absolute;
    left: 0;
    top: 0;
    width: 1200px;
    height: 60px;
    background: linear-gradient(180deg, var(--sky-star) 0%, var(--sky) 100%);
  }
  .contact-band {
    position: absolute;
    left: 0;
    top: 289px;
    width: 1200px;
    height: 61px;
    background: var(--sky);
  }
  .portrait {
    position: absolute;
    left: 0;
    top: 0;
    width: 300px;
    height: 350px;
  }
  .firm-name {
    position: absolute;
    left: 305px;
    top: 85px;
    width: 850px;
    height: 180px;
  }
  .firm-name text {
    font-family: "Alfa Slab One", "Rockwell", serif;
    font-size: 100px;
    fill: var(--white);
  }
  .call-to-action {
    position: absolute;
    left: 391px;
    top: 296px;
    margin: 0;
    display: flex;
    gap: 30px;
    font-family: "Fira Sans Condensed", "Arial Narrow", sans-serif;
    font-weight: 500;
    font-size: 27px;
    line-height: 36px;
    color: var(--white);
    white-space: nowrap;
  }
</style>
</head>
<body>
  <div class="billboard">
    <div class="star-band" role="img" aria-label="Blue band with a pattern of light blue stars"></div>
    <div class="contact-band"></div>

    <svg class="portrait" viewBox="0 0 300 350" role="img" aria-label="Cut-out portrait of the attorney in a grey plaid suit and tie">
      <defs>
        <linearGradient id="portrait-tone" x1="0" y1="0" x2="0" y2="1">
          <stop offset="0" stop-color="#4a3b33"/>
          <stop offset="0.35" stop-color="#c99a82"/>
          <stop offset="0.62" stop-color="#d7dbe2"/>
          <stop offset="1" stop-color="#8d9094"/>
        </linearGradient>
      </defs>
      <path d="M0 60 Q60 25 130 30 A170 170 0 0 1 210 350 L0 350 Z" fill="url(#portrait-tone)"/>
    </svg>

    <svg class="firm-name" viewBox="0 0 850 180" aria-label="Law Offices of Marcus T Whitfield">
      <text x="0" y="80" textLength="848" lengthAdjust="spacingAndGlyphs">LAW OFFICES OF</text>
      <text x="0" y="175" textLength="848" lengthAdjust="spacingAndGlyphs">MARCUS T WHITFIELD</text>
    </svg>

    <p class="call-to-action">
      <span class="tagline">“Don’t go it alone, call today. Arrested?”</span>
      <span class="phone">(555) 384-1927</span>
    </p>
  </div>
</body>
</html>
```